Psychotherapist need a business card with logo

I am a psychotherapist in need of a business card. The card must have:

Moravia Telvundor
Psicoterapeuta
937 218 604

Psychologists use the greek letter psy, which is the psychologist symbol, but I would prefer something like a mandala, a graphic symbol, an iconic tree, nothing very usual, but something that shows confidence and trust.

Industry/Entity Type

Business

```html
<!DOCTYPE html>
<html lang="es">
<head>
<meta charset="UTF-8">
<title>Moravia Telvundor — Tarjeta de visita</title>
<link rel="stylesheet" href="https://fonts.googleapis.com/css2?family=Saira+Condensed:wght@300;400&display=swap">
<style>
  :root {
    --backdrop: #e6e5e3;
    --card: #ffffff;
    --ink: #4a4a4a;
    --ink-soft: #6a6a6a;
    --emblem-faint: #efefef;
    --emblem-mark: #8a8a8a;
    --card-shadow: rgba(0, 0, 0, 0.14);
  }
  * { box-sizing: border-box; margin: 0; padding: 0; }
  html, body {
    width: 1200px;
    height: 1200px;
    overflow: hidden;
    background: var(--backdrop);
    font-family: "Saira Condensed", "Arial Narrow", sans-serif;
  }
  .sheet {
    position: relative;
    width: 1200px;
    height: 1200px;
    display: flex;
    flex-direction: column;
    align-items: center;
    justify-content: center;
    gap: 70px;
  }
  .card {
    position: relative;
    width: 840px;
    height: 480px;
    background: var(--card);
    box-shadow: 0 6px 22px var(--card-shadow);
    overflow: hidden;
  }

  /* Back side: identity corner mark */
  .card-back .corner-mark {
    position: absolute;
    right: 48px;
    bottom: 46px;
    display: flex;
    align-items: center;
    gap: 10px;
    color: var(--emblem-mark);
    font-weight: 400;
    font-size: 22px;
    letter-spacing: 0.04em;
  }
  .corner-mark .mark-dot {
    width: 16px;
    height: 16px;
    border-radius: 50%;
    background: var(--emblem-mark);
  }

  /* Front side */
  .card-front .emblem-faint {
    position: absolute;
    left: 50%;
    top: 50%;
    width: 380px;
    height: 380px;
    transform: translate(-42%, -52%);
  }
  .card-front .name {
    position: absolute;
    left: 0;
    right: 0;
    top: 148px;
    text-align: center;
    color: var(--ink);
    font-weight: 300;
    font-size: 84px;
    line-height: 1;
    letter-spacing: 0.06em;
    text-transform: uppercase;
    word-spacing: 0.2em;
  }
  .card-front .role {
    position: absolute;
    left: 0;
    right: 0;
    top: 250px;
    text-align: center;
    color: var(--ink-soft);
    font-weight: 400;
    font-size: 34px;
    letter-spacing: 0.03em;
  }
  .card-front .phone {
    position: absolute;
    left: 0;
    right: 0;
    top: 322px;
    text-align: center;
    padding-right: 120px;
    color: var(--ink);
    font-weight: 400;
    font-size: 44px;
    letter-spacing: 0.04em;
  }
</style>
</head>
<body>
  <main class="sheet">
    <section class="card card-back" aria-label="Reverso de la tarjeta">
      <div class="corner-mark">
        <span class="mark-dot"></span>
        <span class="mark-name">Moravia Telvundor</span>
      </div>
    </section>

    <section class="card card-front" aria-label="Anverso de la tarjeta">
      <svg class="emblem-faint" viewBox="0 0 100 100" aria-hidden="true">
        <circle cx="50" cy="50" r="48" fill="var(--emblem-faint)"/>
      </svg>
      <h1 class="name">Moravia Telvundor</h1>
      <p class="role">Psicoterapeuta</p>
      <p class="phone">937 218 604</p>
    </section>
  </main>
</body>
</html>
```